Website/Logo Design

We need a logo and website design for an opinion mining startup called VantaLume. Our technology mines the web to automatically discover what people are saying about brands, products, etc. The project we are fielding here is for our informational, public-facing website. In its initial incarnation, it will simply be a vehicle for marketing materials and information on our company and its offerings, but it should be flexible enough to expand as more content/functionality is added.

Some designs we like are:
http://www.tradewhisk.example
http://www.gorvantel.example
http://www.kfz.example
http://www.lintwharf.example
http://moxbarrel.example
http://trundlemq.example
http://www.zopla.example
Updates

All, please try to shy away from using a photo of a person as the focal point of the design.  Our company is more technological than social.

Target Market(s)

Primarily businesses interested in sentiment analysis (typically companies involved in advertising, market research, PR, etc.)

Industry/Entity Type

It Company

Requirements
Must have
• We are looking for a clean, modern, and professional design. This includes a logo, homepage, and internal page if it will differ from the homepage.
Nice to have
• It would be excellent if you could provide an HTML mockup if your design is chosen.
Should not have
• Flash, excessive bells and whistles

```html
<!DOCTYPE html>
<html lang="en">
<head>
<meta charset="utf-8">
<title>VantaLume – About</title>
<link rel="stylesheet" href="https://fonts.googleapis.com/css2?family=Arimo:wght@400;700&display=swap">
<style>
  :root {
    --ink: #3a3a3a;
    --muted: #9a9a9a;
    --brand: #0d5f8e;
    --brand-deep: #0b4f78;
    --sky: #49b6de;
    --rule: #c9c9c9;
    --band: #000000;
    --page: #ffffff;
  }
  * { margin: 0; padding: 0; box-sizing: border-box; }
  html, body { width: 1200px; height: 1197px; overflow: hidden; background: var(--page); }
  body { font-family: "Arimo", Arial, sans-serif; color: var(--ink); position: relative; }

  .band { position: absolute; left: 0; width: 1200px; background: var(--band); }
  .band--top { top: 0; height: 26px; }
  .band--bottom { top: 1135px; height: 62px; }

  .main-nav { position: absolute; left: 81px; top: 106px; list-style: none; }
  .main-nav li { font-size: 20px; line-height: 37px; color: var(--muted); }
  .main-nav li.is-current { color: var(--brand); }

  .wordmark {
    position: absolute; left: 245px; top: 100px; width: 712px; height: 215px;
    display: flex; align-items: center; justify-content: center;
    font-size: 128px; font-weight: 700; letter-spacing: -3px; color: var(--brand);
  }

  .social-link {
    position: absolute; left: 1028px; top: 178px;
    display: flex; align-items: center; gap: 6px;
    font-size: 15px; font-weight: 700; color: var(--sky);
  }
  .social-link .dot { width: 12px; height: 12px; border-radius: 50%; background: var(--sky); }

  .section-title { font-size: 20px; font-weight: 400; color: var(--brand); }

  .news { position: absolute; left: 76px; top: 395px; width: 150px; }
  .news-item { margin-top: 34px; }
  .news-item:first-of-type { margin-top: 36px; }
  .news-date { font-size: 12px; color: var(--brand-deep); margin-bottom: 10px; }
  .news-text { font-size: 12px; line-height: 16px; }
  .news-rule { position: absolute; left: 257px; top: 420px; width: 1px; height: 393px; background: var(--rule); }

  .about { position: absolute; left: 301px; top: 395px; width: 406px; }
  .about .section-title { margin-bottom: 8px; }
  .about p { font-size: 11.6px; line-height: 16px; margin-bottom: 7px; }

  .media { position: absolute; }
  .media--bottles { left: 818px; top: 370px; width: 244px; height: 236px;
    background: radial-gradient(ellipse at 40% 50%, #e6f3f8 0%, #cfe5ef 55%, #ffffff 100%); border-radius: 30px; }
  .media--produce { left: 740px; top: 660px; width: 350px; height: 190px;
    background: linear-gradient(120deg, #c9423a 0%, #e8d6c8 40%, #eef0e4 65%, #b9c48a 100%); border-radius: 18px; }

  .votes { position: absolute; left: 159px; top: 873px; }
  .vote-card { position: absolute; top: 910px; height: 160px; background: #fff;
    box-shadow: 0 3px 6px rgba(0,0,0,.28); padding: 4px; }
  .vote-card div { width: 100%; height: 100%; }
  .vote-card--a { left: 157px; width: 270px; }
  .vote-card--a div { background: linear-gradient(180deg, #ffffff 0%, #eef5fa 60%, #1f8fb6 100%); }
  .vote-card--b { left: 454px; width: 270px; }
  .vote-card--b div { background: linear-gradient(180deg, #2a6fb5 0%, #f4f4f4 25%, #e6e6e6 100%); }
  .vote-card--c { left: 749px; width: 268px; }
  .vote-card--c div { background: linear-gradient(180deg, #1e1e1e 0%, #2a2a2a 25%, #b03020 55%, #d8a030 100%); }
</style>
</head>
<body>
  <div class="band band--top"></div>

  <ul class="main-nav">
    <li>home</li>
    <li class="is-current">about</li>
    <li>rss</li>
    <li>submit</li>
    <li>contact us</li>
  </ul>

  <div class="wordmark">VantaLume</div>

  <div class="social-link"><span class="dot"></span>chirpline</div>

  <section class="news">
    <h2 class="section-title">latest news</h2>
    <article class="news-item">
      <p class="news-date">28 May 2010</p>
      <p class="news-text">molore conse et, sit adipism odolum eu facil dolobore commy nulla vel inci blam dolorerat nonse dipisciduisi</p>
    </article>
    <article class="news-item">
      <p class="news-date">28 May 2010</p>
      <p class="news-text">molore conse et, sit adipism odolum eu facil dolobore commy nulla vel inci blam dolorerat nonse dipisciduis</p>
    </article>
    <article class="news-item">
      <p class="news-date">28 May 2010</p>
      <p class="news-text">molore conse et, sit adipism odolum eu facil dolobore commy nulla faccum alis alisciliquam in vel inci blam dolorerat nonse dipisciduis</p>
    </article>
  </section>
  <div class="news-rule"></div>

  <section class="about">
    <h1 class="section-title">what we do at VantaLume</h1>
    <p>molore conse et, sit adipism odolum eu facil dolobore commy nulla faccum alis alisciliquam in vel inci blam dolorerat nonse dipisciduisi blamcore cor irit am inibh et velent at. Agnibh eu facipis amcore min veniatue commolore et in henim nim quate ex eumsa</p>
    <p>Dolut prat il dolore molore conse et, sit adipism odolum eu facil dolobore commy nulla faccum alis alisciliquam in vel inci blam dolorerat nonse dipisciduisi blamcore cor irit am inibh et velent at. Agnibh eu facipis amcore min veniatue commolore et in henim nim quate ex eumsamolore conse et, sit adipism odolum eu facil dolobore commy nulla faccum alis alisciliquam in vel inci blam dolorerat nonse dipisciduisi blamcore cor irit am inibh et velent at. Agnibh eu facipis amcore min veniatue commolore et in henim nim quate ex eumsa</p>
    <p>Dolut prat il dolore molore conse et, sit adipism odolum eu facil dolobore commy nulla faccum alis alisciliquam in vel inci blam dolorerat nonse dipisciduisi blamcore cor irit am inibh et velent at. Agnibh eu facipis amcore min veniatue commolore et in henim nim quate ex eumsamolore conse et, sit adipism odolum eu facil dolobore commy nulla faccum alis alisciliquam in vel inci blam dolorerat nonse dipisciduisi blamcore cor irit am inibh et velent at. Agnibh eu facipis amcore min veniatue commolore et in henim nim quate ex eumsa</p>
    <p>Dolut prat il dolore molore conse et, sit adipism odolum eu facil dolobore commy nulla faccum alis alisciliquam in vel inci blam dolorerat nonse dipisciduisi blamcore cor irit am inibh et velent at. Agnibh eu facipis amcore min veniatue commolore et in henim nim quate ex eumsa</p>
  </section>

  <div class="media media--bottles" role="img" aria-label="Product photo of two pale blue detergent bottles with orange lettering"></div>
  <div class="media media--produce" role="img" aria-label="Product photo of strawberry punnets with printed paper sleeves"></div>

  <h2 class="section-title votes">public votes</h2>
  <div class="vote-card vote-card--a" role="img" aria-label="Screenshot of a design marketplace homepage"><div></div></div>
  <div class="vote-card vote-card--b" role="img" aria-label="Screenshot of a news website homepage"><div></div></div>
  <div class="vote-card vote-card--c" role="img" aria-label="Screenshot of a web awards site featuring a comic-style campaign"><div></div></div>

  <div class="band band--bottom"></div>
</body>
</html>
```